Web Concept Design - modernize website

Looking to modernize our current website. http :// hvmcoldbrook . com

Color Scheme: Use uploaded palette. (Black, Silver, Dark Purple, Greyish Blue)

The website needs to have a patient-friendly, community-friendly feel to it. While still being a professional medical website. We don't want it to have a cold, clinical feel.

Information on home page needs to be split into their own separate pages with designs for each.

Home Page:
Harborview Walk-In & Family Care is a family practice and urgent care clinic dedicated to providing high quality, compassionate health care, to patients of all ages.
Hours of operation:
Monday-Friday 9am-6:30pm
Saturday: CLOSED
Sunday: CLOSED
Primary Care visits will be by appointment only.
We will accept our last new patient at 6:00p and our last established patient at 6:30p.
We will no longer be doing DOT Physicals.

At bottom of home page:

Harborview Walk-In & Family Care understands that information about your health is private and we know how important it is to keep your medical information protected. We follow all HIPAA guidelines to protect the privacy of your medical records. The privacy act below explains our privacy practices and how we may use and disclose your medical information. If you would like for Harborview Walk-In & Family Care to release any or all of your medical information to others, you can make the request by signing a release and bring it with you at your next visit. If you would like to contact someone about the privacy and/or use of your medical information, you may contact us at 205-381-7260.

Click here for HIPAA document.

Click here for Medical Release form.

---------------

Services Page:
We provide family and urgent care for patients of all ages.

-Annual physicals
-Pre-employment drug screening
-Women's care including pap smears
-Screening and treatment for diabetes, hypertension and cholesterol
-All minor trauma such as abscesses, lacerations, burns and fractures
-Minor skin complaints
-Onsite LAB/XRAY/EKG
-Weight loss
-Adult and Pediatric Vaccinations
-Osteopathic manual medicine
-Medical pain management

-----

Payment & Insurance Page:
We now have online bill pay for patient balances. Please visit https://secure.paytrellixmed.example/hvmc382pay to pay your bill today!

We currently accept all forms of insurance with the exception of Medicaid. Please bring a copy of your insurance card and photo ID upon visit. We are also a Servimed prime provider. We do accept self-pay for patients who do not have insurance.

----

Meet Our Providers Page:

Dr. Daniel (Dan) Whitcomb, DO
Family Practice Physician

Professional Experience
April 4, 2010 to Present Harborview Walk-In & Family Care Owner
12 years of Emergency Medicine experience
6/1994 - 7/1997 KLT Birmingham, AL
Family Medicine Residency
10/1997 to Present Board Certified in Family Medicine
Recertified 2004
Education
9/1990 to 5/1994 Eastbrook College of Osteopathic Medicine
Old Westbury, New York
Degree: Doctor of Osteopathic Medicine
9/1985 to 5/1989 Caldwell-Ridgemont College
Birmingham, Alabama
Degree: Bachelor of Science
Membership
National Guild of Family Practitioners
Physicians Council of the State of Alabama

----

Navigation Bar should have links for all the above pages + NEW PATIENTS + Access Your Medical Records (feel free to be creative with how you design this). We don't want the navigation bar to be too crowded.

Target Market(s)

Medical Patients

Number of Pages Required

5+ page

Colors

Designer to choose colors to be used in the design.

Requirements
Must have
• Designs for all pages
• Keep it professional
Nice to have
• Be creative!
Should not have
• No cold clinical, medical websites

```html
<!DOCTYPE html>
<html lang="en">
<head>
<meta charset="utf-8">
<title>Access Your Medical Records – Harborview Walk-In &amp; Family Care</title>
<link rel="stylesheet" href="https://fonts.googleapis.com/css2?family=Josefin+Sans:wght@700&family=Fira+Sans:wght@400;600;700&family=Signika:wght@600&display=swap">
<style>
  :root {
    --purple: #5e217b;
    --purple-soft: #7a4596;
    --white: #ffffff;
    --ink: #333333;
    --field-text: #3a3a3a;
  }
  * { box-sizing: border-box; margin: 0; padding: 0; }
  html, body { width: 1200px; height: 900px; overflow: hidden; background: var(--white); }
  .page { position: relative; width: 1200px; height: 900px; font-family: "Fira Sans", sans-serif; }

  .contact-row { position: absolute; left: 0; width: 1200px; height: 35px; }
  .contact-row .item { position: absolute; top: 50%; transform: translateY(-50%); display: flex; align-items: center; font-family: "Signika", sans-serif; font-weight: 600; font-size: 12.5px; }
  .contact-row svg { display: block; }
  .contact-row .social { position: absolute; top: 50%; transform: translateY(-50%); width: 29px; height: 29px; border-radius: 50%; border: 1.5px solid currentColor; }
  .topbar { top: 0; color: var(--purple); }

  .header { position: absolute; top: 35px; left: 0; width: 1200px; height: 83px; background: var(--purple); color: var(--white); }
  .brand { position: absolute; left: 17px; top: 12px; font-family: "Josefin Sans", sans-serif; font-weight: 700; font-size: 29px; line-height: 36px; letter-spacing: 0.8px; }
  .main-nav a { position: absolute; top: 32px; color: var(--white); text-decoration: none; font-family: "Signika", sans-serif; font-weight: 600; font-size: 17px; letter-spacing: 0.8px; }

  .subheader { position: absolute; top: 118px; left: 0; width: 1200px; height: 84px; background: var(--white); border-bottom: 2px solid var(--purple); box-shadow: 0 6px 14px rgba(0,0,0,0.12); }
  .hours { position: absolute; left: 19px; color: var(--purple); font-weight: 700; font-size: 21px; }
  .sub-nav a { position: absolute; top: 32px; color: var(--purple); text-decoration: none; font-family: "Signika", sans-serif; font-weight: 600; font-size: 16px; letter-spacing: 0.8px; }

  .page-title { position: absolute; top: 258px; left: 0; width: 1200px; text-align: center; font-family: "Josefin Sans", sans-serif; font-weight: 700; font-size: 52px; letter-spacing: 3px; color: var(--ink); }

  .login-band { position: absolute; top: 355px; left: 0; width: 1200px; height: 316px; background: var(--purple); }
  .login-heading { position: absolute; top: 28px; left: 0; width: 1200px; text-align: center; font-family: "Josefin Sans", sans-serif; font-weight: 700; font-size: 52px; letter-spacing: 2px; color: var(--white); }
  .field { position: absolute; left: 177px; width: 316px; height: 67px; background: var(--white); border: none; padding: 0 9px; font-family: "Fira Sans", sans-serif; font-size: 24px; letter-spacing: 1px; color: var(--field-text); }
  .field::placeholder { color: var(--field-text); }
  .avatar { position: absolute; left: 533px; top: 129px; width: 135px; height: 150px; background: linear-gradient(180deg, var(--white), #ece4f1); border-radius: 60px 60px 8px 8px; }
  .login-button { position: absolute; left: 707px; top: 171px; width: 317px; height: 67px; background: var(--white); border: none; color: var(--purple); font-family: "Josefin Sans", sans-serif; font-weight: 700; font-size: 50px; letter-spacing: 2px; padding-top: 10px; }

  .footer { position: absolute; top: 721px; left: 0; width: 1200px; height: 179px; background: var(--purple); color: var(--white); }
  .footer-about { position: absolute; left: 17px; top: 16px; width: 580px; font-size: 19px; line-height: 19px; letter-spacing: 0.6px; }
  .footer-brand { position: absolute; right: 17px; top: 16px; text-align: right; font-family: "Josefin Sans", sans-serif; font-weight: 700; font-size: 31px; line-height: 37px; letter-spacing: 1px; }
  .footer .contact-row { top: 95px; color: var(--white); }
  .copyright { position: absolute; top: 141px; left: 0; width: 1200px; text-align: center; font-size: 19px; letter-spacing: 0.8px; }
</style>
</head>
<body>
<div class="page">

  <div class="contact-row topbar">
    <div class="item" style="left:18px">
      <svg width="30" height="30" viewBox="0 0 24 24"><path fill="currentColor" d="M6.6 10.8a15.1 15.1 0 0 0 6.6 6.6l2.2-2.2c.3-.3.7-.4 1-.2 1.1.4 2.3.6 3.6.6.6 0 1 .4 1 1V20c0 .6-.4 1-1 1A17 17 0 0 1 3 4c0-.6.4-1 1-1h3.5c.6 0 1 .4 1 1 0 1.3.2 2.5.6 3.6.1.3 0 .7-.2 1z"/></svg>
      <span style="margin-left:20px">205.381.7260</span></div>
    <div class="item" style="left:186px">
      <svg width="32" height="30" viewBox="0 0 24 24"><path fill="currentColor" d="M6 2h12v5H6zM3 8h18a2 2 0 0 1 2 2v7h-4v5H5v-5H1v-7a2 2 0 0 1 2-2zm4 7v5h10v-5zm2 1h6v1H9zm0 2h6v1H9z"/></svg>
      <span style="margin-left:19px">205.447.1938</span></div>
    <div class="item" style="left:355px">
      <svg width="40" height="30" viewBox="0 0 40 30"><rect x="1.5" y="2" width="37" height="26" fill="none" stroke="currentColor" stroke-width="3"/><path d="M2 3l18 15L38 3M2 27l13-12M38 27L25 15" fill="none" stroke="currentColor" stroke-width="3"/></svg>
      <span style="margin-left:20px">harborviewcare@mailbox.example</span></div>
    <div class="item" style="left:625px">
      <svg width="22" height="30" viewBox="0 0 22 30"><path fill="currentColor" d="M11 0a11 11 0 0 0-11 11c0 8 11 19 11 19s11-11 11-19A11 11 0 0 0 11 0zm0 16a5 5 0 1 1 0-10 5 5 0 0 1 0 10z"/></svg>
      <span style="margin-left:20px">2718 Millbrook Road Suite 204&nbsp; Coldbrook, AL 35190</span></div>
    <span class="social" style="left:1056px"></span>
    <span class="social" style="left:1104px"></span>
    <span class="social" style="left:1152px"></span>
  </div>

  <header class="header">
    <div class="brand">HARBORVIEW WALK-IN &amp;<br>FAMILY CARE</div>
    <nav class="main-nav">
      <a href="#" style="left:613px">HOME</a>
      <a href="#" style="left:703px">SERVICES</a>
      <a href="#" style="left:820px">PAYMENT &amp; INSURANCE</a>
      <a href="#" style="left:1049px">OUR PROVIDERS</a>
    </nav>
  </header>

  <div class="subheader">
    <p class="hours" style="top:9px">Monday - Friday: 9am - 6:30pm</p>
    <p class="hours" style="top:46px">Saturday, Sunday: CLOSED</p>
    <nav class="sub-nav">
      <a href="#" style="left:756px">NEW PATIENTS</a>
      <a href="#" style="left:914px">ACCESS YOUR MEDICAL RECORDS</a>
    </nav>
  </div>

  <h1 class="page-title">ACCESS YOUR MEDICAL RECORDS</h1>

  <section class="login-band">
    <h2 class="login-heading">LOG IN</h2>
    <input class="field" style="top:129px" type="text" placeholder="Username or email">
    <input class="field" style="top:213px" type="password" placeholder="Password">
    <div class="avatar" role="img" aria-label="Patient account silhouette icon"></div>
    <button class="login-button" type="button">LOG IN</button>
  </section>

  <footer class="footer">
    <p class="footer-about">Harborview Walk-In &amp; Family Care is a family practice and urgent care clinic dedicated to providing high quality, compassionate health care, to patients of all ages.</p>
    <div class="footer-brand">HARBORVIEW WALK-IN<br>&amp; FAMILY CARE</div>
    <div class="contact-row">
      <div class="item" style="left:17px">
        <svg width="30" height="30" viewBox="0 0 24 24"><path fill="currentColor" d="M6.6 10.8a15.1 15.1 0 0 0 6.6 6.6l2.2-2.2c.3-.3.7-.4 1-.2 1.1.4 2.3.6 3.6.6.6 0 1 .4 1 1V20c0 .6-.4 1-1 1A17 17 0 0 1 3 4c0-.6.4-1 1-1h3.5c.6 0 1 .4 1 1 0 1.3.2 2.5.6 3.6.1.3 0 .7-.2 1z"/></svg>
        <span style="margin-left:20px">205.381.7260</span></div>
      <div class="item" style="left:184px">
        <svg width="32" height="30" viewBox="0 0 24 24"><path fill="currentColor" d="M6 2h12v5H6zM3 8h18a2 2 0 0 1 2 2v7h-4v5H5v-5H1v-7a2 2 0 0 1 2-2zm4 7v5h10v-5zm2 1h6v1H9zm0 2h6v1H9z"/></svg>
        <span style="margin-left:19px">205.447.1938</span></div>
      <div class="item" style="left:353px">
        <svg width="40" height="30" viewBox="0 0 40 30"><rect x="1.5" y="2" width="37" height="26" fill="none" stroke="currentColor" stroke-width="3"/><path d="M2 3l18 15L38 3M2 27l13-12M38 27L25 15" fill="none" stroke="currentColor" stroke-width="3"/></svg>
        <span style="margin-left:20px">harborviewcare@mailbox.example</span></div>
      <div class="item" style="left:623px">
        <svg width="22" height="30" viewBox="0 0 22 30"><path fill="currentColor" d="M11 0a11 11 0 0 0-11 11c0 8 11 19 11 19s11-11 11-19A11 11 0 0 0 11 0zm0 16a5 5 0 1 1 0-10 5 5 0 0 1 0 10z"/></svg>
        <span style="margin-left:20px">2718 Millbrook Road Suite 204&nbsp; Coldbrook, AL 35190</span></div>
      <span class="social" style="left:1054px"></span>
      <span class="social" style="left:1102px"></span>
      <span class="social" style="left:1150px"></span>
    </div>
    <p class="copyright">All rights reserved © 2018. Harborview Walk-In &amp; Family Care</p>
  </footer>

</div>
</body>
</html>
```